Mortgage and Asset Finance Broker Needs a Wordpress Website Design

I need a modern looking Wordpress website to showcase my service as a mortgage and asset broker. I have a company and we work with various lenders to arrange mortgages, as well as commercial lending and business asset finance. The website needs to look professional, be easy to navigate and capture leads. SEO is obviously very important to me. It really needs to be something that shows trust and professioanlism.
Updates

On the home page I will need to have some boxes for Home Loans, Refinancing, Business (and Agriculture) Loans etc. I'd like a carousel in the middle which shows our lenders (so that can have the banks logos added).

It needs to be easy top navigate and showcase all we do - Home Loans, Refinancing, Commercial Loans, Car Loans, Asset Finance etc.

There are plenty of companies on the internet that do this.

There is some good information here https://lendtrellis.com.au/mortgage-broker-homepage/

I need to make sure that editing the website is easy (I think Wordpress has something that allows that).

Also we are very much an Australian business so that is something to advertise.

Industry/Entity Type

Mortgage and Finance Broker

Coding

Coded - Design and coding required

Number of Pages Required

5+ page

Requirements
Must have
• Easy to navigate professional feel. Must be responsive and mobile friendly.
Nice to have
• Homepage with links to inner pages. Contact buttons.

```html
<!DOCTYPE html>
<html lang="en">
<head>
<meta charset="utf-8">
<title>Nexvia Finance – Mortgage &amp; Asset Finance Broker</title>
<link href="https://fonts.googleapis.com/css2?family=Montserrat:wght@400;500;600;700;800&display=swap" rel="stylesheet">
<style>
:root{
  --blue:#17479e;
  --navy:#0f3a86;
  --magenta:#d3105f;
  --purple:#6a2a8e;
  --plum:#a3217f;
  --orange:#f0811f;
  --sky:#e6f0fb;
  --ink:#141414;
  --text:#3a3a3a;
  --white:#ffffff;
}
*{box-sizing:border-box;margin:0;padding:0}
html,body{width:1200px;height:3889px;overflow:hidden}
body{font-family:'Montserrat',sans-serif;color:var(--ink);background:var(--white);position:relative}
.abs{position:absolute}
section,header,footer{position:absolute;left:0;width:1200px;overflow:hidden}
.btn{position:absolute;display:flex;align-items:center;justify-content:center;color:var(--white);font-weight:700;font-size:12px;letter-spacing:.2px;border-radius:0 14px 0 14px}
.arrow{position:absolute;width:34px;height:34px;border-radius:50%;border:1.5px solid #555;background:var(--white);display:flex;align-items:center;justify-content:center}
.arrow svg{width:12px;height:12px}
.eyebrow{color:var(--magenta);font-weight:600;font-size:18px}
.h2{font-weight:700;font-size:41px;line-height:1.15;color:var(--ink)}
.lorem{font-size:11px;line-height:19px;color:var(--text)}

/* header */
.site-header{top:0;height:104px;background:var(--white);box-shadow:0 2px 6px rgba(0,0,0,.05);z-index:5}
.brand{position:absolute;display:flex;align-items:center;gap:10px}
.brand-mark{width:26px;height:26px;border-radius:50%;background:var(--purple)}
.brand-name{font-weight:800;font-size:32px;color:var(--navy);letter-spacing:-.5px}
.nav{position:absolute;left:380px;top:48px;display:flex}
.nav a{font-size:12.5px;font-weight:600;color:var(--ink);text-decoration:none;margin-right:32px}
.nav a.active{color:var(--magenta)}
.call-btn{left:890px;top:37px;width:218px;height:38px;background:var(--plum);font-size:14px;gap:8px;border-radius:0 12px 0 12px}

/* hero */
.hero{top:104px;height:586px;background:var(--sky)}
.hero-title{left:165px;top:150px;font-weight:800;font-size:60px;line-height:1}
.hero-sub{left:165px;top:213px;font-weight:700;font-size:34px;color:var(--magenta)}
.hero-text{left:165px;top:254px;width:350px;font-size:10.5px;line-height:14px;color:var(--text)}
.enquire{left:160px;top:296px;width:130px;height:38px;background:var(--plum)}

/* services */
.services{top:690px;height:320px}
.card{position:absolute;width:206px;height:330px;border-radius:14px;overflow:hidden;border:4px solid}
.card .photo{position:absolute;left:0;top:0;width:100%;height:222px}
.card .icon{position:absolute;left:50%;top:180px;transform:translateX(-50%);width:76px;height:76px;border-radius:50%;background:var(--white);display:flex;align-items:center;justify-content:center}
.card .icon span{width:56px;height:56px;border-radius:50%;display:flex;align-items:center;justify-content:center}
.card .label{position:absolute;left:0;width:100%;top:260px;text-align:center;color:var(--white);font-weight:700;font-size:18px;line-height:24px}

/* about */
.about{top:1010px;height:517px}
.about-frame{left:160px;top:53px;width:355px;height:362px;border:5px solid var(--blue);border-radius:8px;overflow:hidden}
.years{left:422px;top:295px;width:163px;height:163px;background:var(--blue);border-radius:12px;color:var(--white);text-align:center;padding-top:14px}
.years b{display:block;font-size:64px;line-height:70px;font-weight:800}
.years span{display:block;font-size:19px;line-height:24px;font-weight:600}

/* lenders */
.lenders{top:1527px;height:198px;background:var(--sky)}
.lender{position:absolute;top:60px;width:110px;height:66px;display:flex;flex-direction:column;align-items:center;gap:8px}
.lender i{display:block;width:40px;height:34px;border-radius:6px}
.lender em{display:block;width:96px;height:9px;border-radius:4px;background:#3c4a5c;opacity:.7}

/* features */
.features{top:1725px;height:558px;background:var(--white)}
.feat-icon{width:56px;height:56px;flex:none;border-radius:50%;border:1.5px solid var(--magenta);display:flex;align-items:center;justify-content:center}
.feat h3{font-size:20px;font-weight:600;margin-bottom:6px}

/* testimonials */
.testimonials{top:2283px;height:620px;background:var(--sky)}
.quote-card{position:absolute;top:229px;width:280px;height:224px;background:var(--white);border-radius:8px;text-align:center;padding:56px 22px 0}
.quote-card p{font-size:11.5px;line-height:15px;color:var(--text)}
.quote-card b{display:block;margin-top:14px;font-size:14px;font-weight:700}
.quote-badge{position:absolute;top:-28px;left:50%;transform:translateX(-50%);width:58px;height:58px;border-radius:50%;background:var(--white);box-shadow:0 3px 8px rgba(0,0,0,.12);display:flex;align-items:center;justify-content:center;color:var(--blue);font-size:44px;font-weight:800;line-height:1;padding-top:16px}

/* faq */
.faq{top:2903px;height:642px;background:var(--white)}
.faq-item{position:absolute;left:174px;width:852px;height:57px;background:var(--blue);border-radius:3px;color:var(--white);font-size:22px;font-weight:600;display:flex;align-items:center;padding-left:26px}
.faq-item .chev{position:absolute;right:18px;top:14px;width:30px;height:30px;border-radius:50%;border:1.5px solid rgba(255,255,255,.8);display:flex;align-items:center;justify-content:center}
.faq-answer{position:absolute;left:174px;width:852px;height:88px;background:#edf3fb;padding:24px 30px;font-size:12px;line-height:19px;color:var(--text)}

/* footer */
.site-footer{top:3545px;height:344px;background:var(--blue);color:var(--white)}
.site-footer h4{font-size:14px;font-weight:700;margin-bottom:14px}
.site-footer li{list-style:none;font-size:11.5px;line-height:22.5px;display:flex;align-items:center;gap:10px}
.site-footer li::before{content:"✕";font-size:10px;font-weight:800}
.social{display:flex;gap:10px}
.social span{width:30px;height:30px;border-radius:50%;border:1.3px solid rgba(255,255,255,.85)}
</style>
</head>
<body>

<header class="site-header">
  <div class="brand" style="left:150px;top:30px">
    <span class="brand-mark"></span>
    <span class="brand-name">Nexvia</span>
  </div>
  <nav class="nav">
    <a class="active" href="#">HOME</a>
    <a href="#">ABOUT</a>
    <a href="#">SERVICES</a>
    <a href="#">BLOG</a>
    <a href="#">FAQS</a>
    <a href="#">CONTACT US</a>
  </nav>
  <div class="btn call-btn">
    <svg width="15" height="15" viewBox="0 0 24 24"><path fill="#fff" d="M6.6 10.8a15 15 0 006.6 6.6l2.2-2.2a1 1 0 011-.25 11.4 11.4 0 003.6.6 1 1 0 011 1V20a1 1 0 01-1 1A17 17 0 013 4a1 1 0 011-1h3.5a1 1 0 011 1c0 1.25.2 2.45.57 3.57a1 1 0 01-.25 1z"/></svg>
    CALL : 1800 555 017
  </div>
</header>

<section class="hero">
  <svg class="abs" style="left:0;top:0" width="1200" height="586" viewBox="0 0 1200 586">
    <polygon points="447,0 900,0 900,470 760,586 447,140" fill="#17479e"/>
    <polygon points="620,0 1110,0 870,586 430,586" fill="#6a2a8e"/>
    <polygon points="930,0 1110,0 940,250" fill="#d3105f"/>
    <polygon points="1010,330 1200,520 1200,586 1080,586 960,450" fill="#f0811f"/>
  </svg>
  <div class="abs" role="img" aria-label="Smiling family of three, father carrying his daughter on his back" style="left:590px;top:0;width:460px;height:586px;background:linear-gradient(160deg,#3a4a6c 0%,#6b5a52 45%,#2f4c78 100%);clip-path:polygon(12% 0,100% 0,100% 100%,0 100%)"></div>
  <div class="abs hero-title">Nexvia</div>
  <div class="abs hero-sub">Finance</div>
  <p class="abs hero-text">Lorem ipsum dolor sit amet, consectetur adipiscing elit, sed do eiusmod tempor incididunt ut labore et dolore magna aliqua.</p>
  <div class="btn enquire">ENQUIRE NOW</div>
  <div class="arrow" style="left:180px;top:409px;background:var(--orange);border-color:var(--orange)"><svg viewBox="0 0 12 12"><path d="M8 2L4 6l4 4" stroke="#fff" stroke-width="2" fill="none"/></svg></div>
  <div class="arrow" style="left:224px;top:409px"><svg viewBox="0 0 12 12"><path d="M4 2l4 4-4 4" stroke="#333" stroke-width="2" fill="none"/></svg></div>
</section>

<section class="services">
  <div class="arrow" style="left:112px;top:88px"><svg viewBox="0 0 12 12"><path d="M8 2L4 6l4 4" stroke="#333" stroke-width="2" fill="none"/></svg></div>
  <div class="arrow" style="left:1053px;top:88px"><svg viewBox="0 0 12 12"><path d="M4 2l4 4-4 4" stroke="#333" stroke-width="2" fill="none"/></svg></div>
</section>

<div class="card" style="left:160px;top:630px;background:var(--blue);border-color:var(--blue)">
  <div class="photo" role="img" aria-label="Model house beside stacks of coins" style="background:linear-gradient(180deg,#c9b59a,#7a6a5a)"></div>
  <div class="icon"><span style="background:var(--blue)"><svg width="30" height="30" viewBox="0 0 24 24"><path d="M3 11l9-7 9 7v9H3z" fill="none" stroke="#fff" stroke-width="1.8"/></svg></span></div>
  <div class="label">HOME LOAN</div>
</div>
<div class="card" style="left:386px;top:630px;background:var(--magenta);border-color:var(--magenta)">
  <div class="photo" role="img" aria-label="Wooden blocks reading business loan" style="background:linear-gradient(180deg,#5a4a40,#8a6a48)"></div>
  <div class="abs" style="left:22px;top:50px;width:156px;color:#fff;font-size:9.5px;line-height:12px;text-align:center">Lorem ipsum dolor sit amet, consectetur adipiscing elit, sed do eiusmod tempor incididunt ut labore.</div>
  <div class="icon"><span style="background:var(--magenta)"><svg width="28" height="28" viewBox="0 0 24 24"><rect x="5" y="3" width="14" height="18" rx="2" fill="none" stroke="#fff" stroke-width="1.8"/><path d="M8 8h8M8 12h8M8 16h5" stroke="#fff" stroke-width="1.6"/></svg></span></div>
  <div class="label">COMMERCIAL<br>LOANS</div>
</div>
<div class="card" style="left:611px;top:630px;background:var(--purple);border-color:var(--purple)">
  <div class="photo" role="img" aria-label="Toy car resting on loan paperwork" style="background:linear-gradient(180deg,#b9b4ac,#4a6080)"></div>
  <div class="icon"><span style="background:var(--purple)"><svg width="30" height="30" viewBox="0 0 24 24"><path d="M4 15l2-5h12l2 5v4H4z" fill="none" stroke="#fff" stroke-width="1.8"/><circle cx="8" cy="17" r="1.3" fill="#fff"/><circle cx="16" cy="17" r="1.3" fill="#fff"/></svg></span></div>
  <div class="label">CAR LOANS</div>
</div>
<div class="card" style="left:836px;top:630px;background:var(--orange);border-color:var(--orange)">
  <div class="photo" role="img" aria-label="Finance growth graphic with money bag and charts" style="background:linear-gradient(180deg,#3a3f4a,#b26a2a)"></div>
  <div class="icon"><span style="background:var(--orange)"><svg width="30" height="30" viewBox="0 0 24 24"><path d="M4 20V10M10 20V6M16 20v-8M22 20H2" stroke="#fff" stroke-width="1.8" fill="none"/></svg></span></div>
  <div class="label">ASSET FINANCE</div>
</div>

<section class="about">
  <svg class="abs" style="left:0;top:30px" width="380" height="500" viewBox="0 0 380 500">
    <polygon points="0,60 80,140 0,230" fill="#17479e"/>
    <polygon points="0,230 160,80 160,260 0,320" fill="#d3105f" opacity=".85"/>
    <polygon points="0,320 160,260 0,420" fill="#a3217f"/>
    <polygon points="0,330 80,400 0,490" fill="#6a2a8e"/>
    <polygon points="110,400 200,320 375,490 250,490" fill="#f0811f"/>
  </svg>
  <div class="abs about-frame" role="img" aria-label="Couple standing in front of their new home" style="background:linear-gradient(180deg,#8a7a68,#6a6a40 70%,#3f4a2a)"></div>
  <div class="abs years"><b>20</b><span>Years</span><span>of Service</span></div>
  <div class="abs eyebrow" style="left:608px;top:25px">About Us</div>
  <h2 class="abs h2" style="left:608px;top:52px">Explore Our<br>Mortgage Solutions</h2>
  <p class="abs lorem" style="left:608px;top:170px;width:450px">Lorem ipsum dolor sit amet, consectetur adipiscing elit, sed do eiusmod tempor incididunt ut labore et dolore magna aliqua. Quis ipsum suspendisse ultrices gravida. Risus commodo viverra maecenas accumsan Quis ipsum suspendisse ultrices gravida. Risus commodo viverra maecenas accumsan</p>
  <p class="abs lorem" style="left:608px;top:264px;width:450px">Lorem ipsum dolor sit amet, consectetur adipiscing elit, sed do eiusmod tempor incididunt ut labore et dolore magna aliqua. Quis ipsum suspendisse ultrices gravida. Risus commodo viverra maecenas accumsanis. Quis ipsum suspendisse ultrices gravida. Risus commodo viverra maecenas accumsan</p>
  <div class="btn" style="left:606px;top:362px;width:198px;height:38px;background:var(--navy)">MAKE AN APPOINTMENT</div>
</section>

<section class="lenders">
  <div class="arrow" style="left:114px;top:88px"><svg viewBox="0 0 12 12"><path d="M8 2L4 6l4 4" stroke="#333" stroke-width="2" fill="none"/></svg></div>
  <div class="arrow" style="left:1053px;top:81px"><svg viewBox="0 0 12 12"><path d="M4 2l4 4-4 4" stroke="#333" stroke-width="2" fill="none"/></svg></div>
  <div class="lender" style="left:180px"><i style="background:#4a9a3a"></i><em></em></div>
  <div class="lender" style="left:316px"><i style="background:#2d5c9a"></i><em></em></div>
  <div class="lender" style="left:459px"><i style="background:#c9372c"></i><em></em></div>
  <div class="lender" style="left:595px"><i style="background:#2c3540"></i><em></em></div>
  <div class="lender" style="left:742px"><i style="background:#b02a3a"></i><em></em></div>
  <div class="lender" style="left:892px"><i style="background:#4a9aa0"></i><em></em></div>
</section>

<section class="features">
  <svg class="abs" style="left:0;top:0" width="620" height="558" viewBox="0 0 620 558">
    <polygon points="120,0 335,0 0,330 0,120" fill="#f6c8dc" opacity=".8"/>
    <polygon points="0,360 160,300 0,480" fill="#e9d3ef"/>
    <polygon points="120,300 335,558 120,558" fill="#fde1c3" opacity=".9"/>
  </svg>
  <div class="abs" role="img" aria-label="Advisor and client smiling while reviewing documents at a laptop" style="left:620px;top:0;width:580px;height:558px;background:linear-gradient(135deg,#d8d0c6 0%,#8aa0c0 50%,#c9b0a0 100%);clip-path:polygon(24% 0,100% 0,100% 100%,24% 100%,0 44%)"></div>
  <svg class="abs" style="left:630px;top:0" width="170" height="558" viewBox="0 0 170 558"><path d="M160 0L0 258l160 300" stroke="#17479e" stroke-width="3" fill="none"/></svg>
  <div class="abs eyebrow" style="left:166px;top:110px">Our Features</div>
  <h2 class="abs h2" style="left:165px;top:135px">Quick Easy Flexible</h2>
  <div class="abs feat" style="left:165px;top:208px;display:flex;gap:22px">
    <div class="feat-icon"><svg width="28" height="28" viewBox="0 0 24 24"><circle cx="12" cy="12" r="8" fill="none" stroke="#d3105f" stroke-width="1.5"/><path d="M14.5 9.5c-.5-1-1.5-1.3-2.5-1.3-1.4 0-2.4.7-2.4 1.8 0 2.5 5 1.3 5 3.9 0 1.1-1 1.9-2.6 1.9-1.1 0-2.1-.5-2.6-1.4M12 6.5v11" stroke="#d3105f" stroke-width="1.4" fill="none"/></svg></div>
    <div><h3>Lower Rates</h3><p class="lorem" style="width:320px">Lorem ipsum dolor sit amet, consectetur adipiscing elit, sed do eiusmod tempor incididunt ut labore et dolore magna aliqua.</p></div>
  </div>
  <div class="abs feat" style="left:165px;top:315px;display:flex;gap:22px">
    <div class="feat-icon"><svg width="28" height="28" viewBox="0 0 24 24"><path d="M19 12a7 7 0 01-12 5M5 12a7 7 0 0112-5M17 3v4h-4M7 21v-4h4" stroke="#d3105f" stroke-width="1.5" fill="none"/></svg></div>
    <div><h3>Easy Process</h3><p class="lorem" style="width:320px">Lorem ipsum dolor sit amet, consectetur adipiscing elit, sed do eiusmod tempor incididunt ut labore et dolore magna aliqua.</p></div>
  </div>
  <div class="btn" style="left:175px;top:435px;width:124px;height:38px;background:#2b4f84">LEARN MORE</div>
</section>

<section class="testimonials">
  <div class="abs eyebrow" style="left:0;width:1200px;text-align:center;top:82px">Testimonials</div>
  <h2 class="abs h2" style="left:0;width:1200px;text-align:center;top:112px">What Our Customer says</h2>
  <div class="quote-card" style="left:160px"><div class="quote-badge">”</div><p>Lorem ipsum dolor sit amet, consectetur adipiscing elit, sed do eiusmod tempor incididunt ut labore et dolore magna aliqua. Quis ipsum suspendisse ultrices gravida. Risus commodo viverra maecenas accumsan lacus vel facilisis.</p><b>- Harriet</b></div>
  <div class="quote-card" style="left:460px"><div class="quote-badge">”</div><p>Lorem ipsum dolor sit amet, consectetur adipiscing elit, sed do eiusmod tempor incididunt ut labore et dolore magna aliqua. Quis ipsum suspendisse ultrices gravida. Risus commodo viverra maecenas accumsan lacus vel facilisis.</p><b>- Priya</b></div>
  <div class="quote-card" style="left:760px"><div class="quote-badge">”</div><p>Lorem ipsum dolor sit amet, consectetur adipiscing elit, sed do eiusmod tempor incididunt ut labore et dolore magna aliqua. Quis ipsum suspendisse ultrices gravida. Risus commodo viverra maecenas accumsan lacus vel facilisis.</p><b>- Sophie</b></div>
  <div class="arrow" style="left:561px;top:488px"><svg viewBox="0 0 12 12"><path d="M8 2L4 6l4 4" stroke="#333" stroke-width="2" fill="none"/></svg></div>
  <div class="arrow" style="left:605px;top:488px"><svg viewBox="0 0 12 12"><path d="M4 2l4 4-4 4" stroke="#333" stroke-width="2" fill="none"/></svg></div>
</section>

<section class="faq">
  <svg class="abs" style="left:0;top:0" width="1200" height="642" viewBox="0 0 1200 642">
    <polygon points="640,0 940,0 1120,170 900,170" fill="#dfe7f3"/>
    <polygon points="1200,0 1200,180 1100,120" fill="#f6cfe0"/>
    <polygon points="950,200 1200,60 1200,420 1080,380" fill="#ecd7ea" opacity=".8"/>
    <polygon points="1090,420 1200,300 1200,600" fill="#fde4c9"/>
    <polygon points="600,642 760,500 900,642" fill="#eadcf0"/>
    <polygon points="0,200 80,120 0,60" fill="#f3e4f0"/>
  </svg>
  <h2 class="abs" style="left:0;width:1200px;text-align:center;top:62px;font-size:40px;font-weight:700">FAQ</h2>
  <div class="faq-item" style="top:147px">Lorem ipsum dolor sit amet, consectetur adipiscing?<span class="chev"><svg width="12" height="12" viewBox="0 0 12 12"><path d="M2 8l4-4 4 4" stroke="#fff" stroke-width="1.6" fill="none"/></svg></span></div>
  <div class="faq-answer" style="top:204px">Lorem ipsum dolor sit amet, consectetur adipiscing elit, sed do eiusmod tempor incididunt ut labore et dolore magna aliqua. Quis ipsum suspendisse ultrices gravida. Risus commodo viverra maecenas accumsan lacus vel facilisis.</div>
  <div class="faq-item" style="top:297px">Lorem ipsum dolor sit amet, consectetur adipiscing?<span class="chev"><svg width="12" height="12" viewBox="0 0 12 12"><path d="M2 4l4 4 4-4" stroke="#fff" stroke-width="1.6" fill="none"/></svg></span></div>
  <div class="faq-item" style="top:361px">Lorem ipsum dolor sit amet, consectetur adipiscing?<span class="chev"><svg width="12" height="12" viewBox="0 0 12 12"><path d="M2 4l4 4 4-4" stroke="#fff" stroke-width="1.6" fill="none"/></svg></span></div>
  <div class="faq-item" style="top:425px">Lorem ipsum dolor sit amet, consectetur adipiscing?<span class="chev"><svg width="12" height="12" viewBox="0 0 12 12"><path d="M2 4l4 4 4-4" stroke="#fff" stroke-width="1.6" fill="none"/></svg></span></div>
  <div class="faq-item" style="top:489px">Lorem ipsum dolor sit amet, consectetur adipiscing?<span class="chev"><svg width="12" height="12" viewBox="0 0 12 12"><path d="M2 4l4 4 4-4" stroke="#fff" stroke-width="1.6" fill="none"/></svg></span></div>
</section>

<footer class="site-footer">
  <div class="brand" style="left:190px;top:75px">
    <span class="brand-mark" style="background:#fff"></span>
    <span class="brand-name" style="color:#fff">Nexvia</span>
  </div>
  <p class="abs" style="left:181px;top:140px;width:240px;font-size:10.5px;line-height:15px">Lorem ipsum dolor sit amet, consectetur adipiscing elit, sed do eiusmod tempor incididunt ut labore et dolore magna aliqua. Quis ipsum suspendisse.</p>
  <div class="abs social" style="left:183px;top:216px"><span></span><span></span><span></span><span></span></div>
  <div class="abs" style="left:503px;top:92px"><h4>Quick Links</h4><ul><li>Home</li><li>About Us</li><li>Services</li><li>Blog</li><li>FAQ</li><li>Contact Us</li></ul></div>
  <div class="abs" style="left:672px;top:92px"><h4>Services</h4><ul><li>Home Loan</li><li>Business Loan</li><li>Refinance</li><li>Car Loan</li><li>Asset Finance</li></ul></div>
  <div class="abs" style="left:835px;top:92px;font-size:11.5px;line-height:22px">
    <h4>Contact Us</h4>
    <div style="display:flex;gap:10px"><svg width="10" height="14" viewBox="0 0 10 14" style="margin-top:4px"><path d="M5 0a5 5 0 00-5 5c0 4 5 9 5 9s5-5 5-9a5 5 0 00-5-5z" fill="#fff"/><circle cx="5" cy="5" r="1.8" fill="#17479e"/></svg><span>88 Harbour Lane<br>Sydney 2000</span></div>
    <div style="display:flex;gap:8px;margin-top:8px;font-weight:700;font-size:14px;align-items:center"><svg width="13" height="13" viewBox="0 0 24 24"><path fill="#fff" d="M6.6 10.8a15 15 0 006.6 6.6l2.2-2.2a1 1 0 011-.25 11.4 11.4 0 003.6.6 1 1 0 011 1V20a1 1 0 01-1 1A17 17 0 013 4a1 1 0 011-1h3.5a1 1 0 011 1c0 1.25.2 2.45.57 3.57a1 1 0 01-.25 1z"/></svg>CALL : 1800 555 017</div>
    <div style="display:flex;gap:8px;margin-top:6px;align-items:center"><svg width="12" height="10" viewBox="0 0 12 10"><rect width="12" height="10" rx="1" fill="#fff"/><path d="M0 1l6 4 6-4" stroke="#17479e" fill="none"/></svg>info@nexvia.com</div>
  </div>
  <div class="abs" style="left:0;width:1200px;text-align:center;top:310px;font-size:10.5px">© 2025 | www.nexvia.com</div>
</footer>

</body>
</html>
```